Web Design Project

Need a web design to be built by in-house team of developers. I need the look and feel of the site done ready for the developers to take over.

The site is a crowd funding site like www.pledgeloft.example. Our site will have all the main functions provided for on this site.
We are not looking for sophisticated investors, instead we are looking for people with an interest in investing but that need a lot of help and support through the process.

I have already obtained the logo. I attach it here.

I also want to have a coming soon page designed. I have sketched out what i want here and am uploading it in excel. this is obviously very basic and not what i will want for the main site.

colours should be light and accessible: blues, greens, yellows.

Site is to be fun and accessible.

site will have a lot of communication based aspects needed.

I am looking for a long term relationship with a designer to do this and to do many more things. I will have a lot of banners and desgin work to do here, and am looking ONLY for someone that can work on an ongoing basis (not full time, but a few hours a week).

I am also after an animation - basic 2 minute intro - not full animation, part powerpoint and part animation. I have made a separate tender for this, please quote me on it. I want the same person doing them all preferably....
Updates

Hi all

I am impressed with some of these designs. I have uploaded the wireframe of the coming soon page. 

I prefer the designs so far that are utilizing our little icons etc. 

obviously i understand you havent got root access or anything yet so are struggling to put them in, but its worth a try, some of the designs are using them well. 

i like bright colours. 

i would also show me how you are going to design other aspects eg chat box, forum page etc. 

Industry/Entity Type

Communication

Requirements
Must have
• the site will have all the functions of www.pledgeloft.example and www.venturibay.example.

```html
<!DOCTYPE html>
<html lang="en">
<head>
<meta charset="utf-8">
<title>Ideaora Forum</title>
<link href="https://fonts.googleapis.com/css2?family=Questrial&display=swap" rel="stylesheet">
<style>
:root{
  --sky:#2f82bd;
  --tab:#5aaadf;
  --panel:#d4e6f4;
  --panel-line:#b7d3ea;
  --bar:#5aa9dc;
  --link:#1f7ab5;
  --ink:#333d46;
  --muted:#6e8394;
  --white:#ffffff;
  --wash:#eef5fb;
  --amber:#f7a531;
}
*{box-sizing:border-box;margin:0;padding:0}
html,body{width:1200px;height:916px;overflow:hidden}
body{position:relative;font-family:"Questrial",sans-serif;color:var(--ink);
  background:linear-gradient(var(--white) 75px,var(--wash) 600px,#e3eff8 805px)}
.abs{position:absolute}
.topband{left:0;top:0;width:1200px;height:75px;background:var(--sky)}
.brand-card{left:197px;top:12px;width:166px;height:100px;background:var(--white);border-radius:8px 8px 0 0;text-align:center;padding-top:40px}
.brand-mark{display:inline-block;width:12px;height:12px;background:var(--sky);margin-right:6px;vertical-align:middle}
.brand-name{font-size:22px;color:#2b3a45;letter-spacing:1px;vertical-align:middle}
.brand-tag{font-size:8px;color:#555;margin-top:3px;letter-spacing:.3px}
.press{left:236px;top:120px;font-size:14px;color:#8a8a8a;font-weight:700}
.nav{left:525px;top:47px;display:flex;gap:2px}
.nav a{height:28px;line-height:28px;padding:0 13px;background:var(--tab);color:var(--white);font-size:12px;text-decoration:none;border-radius:2px 2px 0 0}
.nav a.active{background:var(--white);color:#334;padding:0 15px}
.nav svg{vertical-align:-2px}
.login{left:197px;top:144px;width:822px;height:31px;border:1px solid var(--panel-line);border-radius:4px;background:var(--white);font-size:11px;color:var(--link)}
.login span,.login .field,.login .signup,.login .sep{position:absolute;top:8px}
.login .field{top:5px;height:20px;width:206px;border:1px solid var(--panel-line);border-radius:2px}
.login .sep{width:1px;height:15px;background:var(--link);top:7px}
.login .signup{top:3px;left:678px;width:128px;height:23px;border-radius:2px;background:linear-gradient(#d8eef9,#a9d6ee);color:#234;text-align:center;line-height:22px;border:1px solid #9cc8e2}
.banner{left:197px;top:182px;width:822px;height:37px;background:var(--bar);border:1px solid #3f8fc6;border-radius:5px;color:var(--white);font-size:13px;text-align:center;line-height:36px}
.banner b{font-weight:400;margin-right:10px}
.banner i{font-style:normal;font-size:15px;margin-left:12px;letter-spacing:.5px}
.panel{left:197px;top:240px;width:822px;height:420px;background:var(--panel);border:1px solid var(--panel-line);border-radius:6px}
.panel h1{position:absolute;left:23px;top:12px;font-size:15px;color:var(--link);font-weight:700}
.see-more{left:943px;top:639px;font-size:9px;color:var(--link);font-weight:700}
.forum{left:223px;top:284px;width:772px;height:344px;background:var(--bar);border-radius:3px;padding:0 4px 4px}
.forum-head{height:24px;color:var(--white);font-size:11px;font-weight:700;position:relative}
.forum-head span{position:absolute;top:6px}
.rows{background:var(--white)}
.row{height:39.5px;position:relative;border-bottom:1px solid var(--bar);font-size:9.5px}
.row:last-child{border-bottom:0}
.row svg{position:absolute;left:10px;top:9px}
.row .title{position:absolute;left:48px;top:6px;font-size:11px;color:var(--link);font-weight:700}
.row .desc{position:absolute;left:48px;top:21px;color:var(--ink)}
.row .num{position:absolute;top:15px;width:60px;text-align:center}
.row .c{left:340px}.row .v{left:419px}
.row .act{position:absolute;left:521px;top:7px;line-height:13px}
.row .act b{color:var(--link)}
.row .div{position:absolute;top:4px;bottom:4px;width:1px;background:#e1e7ec}
.foot-links{left:0;width:1200px;top:769px;text-align:center;font-size:11px;color:var(--muted)}
.foot-links a{color:var(--muted);text-decoration:none;margin:0 6px}
.sea{left:0;top:800px;width:1200px;height:116px}
.pay-card{left:64px;top:839px;width:287px;height:77px;background:var(--white);border-radius:4px 4px 0 0}
.pay-name{position:absolute;left:43px;top:12px;font-size:15px;color:#213a74;font-weight:700}
.pay-strip{position:absolute;left:26px;top:32px;width:231px;height:36px;border:2px solid var(--amber);border-radius:3px;padding:6px 5px;display:flex;gap:5px}
.pay-strip i{display:block;width:30px;height:20px;background:#cfd8e3;border-radius:2px}
.social{top:843px;color:var(--white);font-size:12px;font-weight:700;display:flex;align-items:center;gap:8px}
.social i{display:block;width:30px;height:30px;border-radius:4px;background:#6cc0ea}
.copy{left:1058px;top:856px;font-size:10px;color:var(--white)}
.char{border-radius:40px 40px 8px 8px}
</style>
</head>
<body>
<div class="abs topband"></div>

<div class="abs brand-card">
  <span class="brand-mark"></span><span class="brand-name">IDEAORA</span>
  <div class="brand-tag">BRIGHT PLANS START HERE</div>
</div>
<div class="abs press">Startup Lantern</div>

<nav class="abs nav">
  <a href="#"><svg width="12" height="12" viewBox="0 0 12 12"><path d="M6 1 0 6h2v5h3V8h2v3h3V6h2z" fill="#fff"/></svg></a>
  <a href="#">Invest</a><a href="#">Get Investment</a><a href="#">How it Works</a><a href="#">About Us</a><a href="#">Blog</a><a href="#" class="active">Forum</a>
</nav>

<div class="abs login">
  <span style="left:13px">LOGIN</span><div class="sep" style="left:68px"></div>
  <span style="left:82px">Username:</span><div class="field" style="left:142px"></div>
  <span style="left:369px">Password:</span><div class="field" style="left:429px"></div>
  <div class="sep" style="left:654px"></div>
  <div class="signup">Sign Up</div>
</div>

<div class="abs banner"><b>You need to be a member to use the Forum.</b>Not a member? <i>Sign up here ↗</i></div>

<section class="abs panel"><h1>Welcome to our Forum!</h1></section>
<a class="abs see-more">... see more</a>

<div class="abs forum">
  <div class="forum-head">
    <span style="left:48px">Main Discussions</span><span style="left:344px">Comments</span><span style="left:434px">Views</span><span style="left:521px">Last Activity</span>
  </div>
  <div class="rows">
    <div class="row"><svg width="22" height="22" viewBox="0 0 22 22"><path d="M1 1h20v14H9l-6 5v-5H1z" fill="none" stroke="#5aa9dc"/></svg><div class="div" style="left:331px"></div><div class="div" style="left:409px"></div><span class="title">Investor Discussions...</span><span class="desc">Discussions about the ins and outs of Investing</span><span class="num c">48</span><span class="num v">1245</span><span class="act">23 August 2011 &nbsp;- &nbsp;8:45 AM<br>By <b>LucyJ</b></span></div>
    <div class="row"><svg width="22" height="22" viewBox="0 0 22 22"><path d="M1 1h20v14H9l-6 5v-5H1z" fill="none" stroke="#5aa9dc"/></svg><div class="div" style="left:331px"></div><div class="div" style="left:409px"></div><span class="title">Funding Your Business...</span><span class="desc">Getting other Investors to fund your business</span><span class="num c">23</span><span class="num v">366</span><span class="act">22 August 2011 &nbsp;- &nbsp;2:13 PM<br>By <b>Randal02</b></span></div>
    <div class="row"><svg width="22" height="22" viewBox="0 0 22 22"><path d="M1 1h20v14H9l-6 5v-5H1z" fill="none" stroke="#5aa9dc"/></svg><div class="div" style="left:331px"></div><div class="div" style="left:409px"></div><span class="title">Investing in Others Ideas...</span><span class="desc">Is Investing in others big ideas worth it?</span><span class="num c">5</span><span class="num v">234</span><span class="act">22 August 2011 &nbsp;- &nbsp;6:21 AM<br>By <b>MichaelS41</b></span></div>
    <div class="row"><svg width="22" height="22" viewBox="0 0 22 22"><path d="M1 1h20v14H9l-6 5v-5H1z" fill="none" stroke="#5aa9dc"/></svg><div class="div" style="left:331px"></div><div class="div" style="left:409px"></div><span class="title">Investing is the right thing...</span><span class="desc">Discussions about Investing in others growth</span><span class="num c">30</span><span class="num v">581</span><span class="act">20 August 2011 &nbsp;- &nbsp;7:50 PM<br>By <b>Louis_22</b></span></div>
    <div class="row"><svg width="22" height="22" viewBox="0 0 22 22"><path d="M1 1h20v14H9l-6 5v-5H1z" fill="none" stroke="#5aa9dc"/></svg><div class="div" style="left:331px"></div><div class="div" style="left:409px"></div><span class="title">Past Business Successes...</span><span class="desc">Chatting about businesses who used Ideaora</span><span class="num c">11</span><span class="num v">698</span><span class="act">18 August 2011 &nbsp;- &nbsp;12:42 PM<br>By <b>JasonM_696</b></span></div>
    <div class="row"><svg width="22" height="22" viewBox="0 0 22 22"><path d="M1 1h20v14H9l-6 5v-5H1z" fill="none" stroke="#5aa9dc"/></svg><div class="div" style="left:331px"></div><div class="div" style="left:409px"></div><span class="title">Entrepreneurs and Investors...</span><span class="desc">Discussions from both points of view</span><span class="num c">16</span><span class="num v">411</span><span class="act">16 August 2011 &nbsp;- &nbsp;3:26 AM<br>By <b>JoeSoap01</b></span></div>
    <div class="row"><svg width="22" height="22" viewBox="0 0 22 22"><path d="M1 1h20v14H9l-6 5v-5H1z" fill="none" stroke="#5aa9dc"/></svg><div class="div" style="left:331px"></div><div class="div" style="left:409px"></div><span class="title">How to start your Business...</span><span class="desc">Advice on how to ensure your business works</span><span class="num c">67</span><span class="num v">1036</span><span class="act">15 August 2011 &nbsp;- &nbsp;8:02 PM<br>By <b>LuckY-StaR</b></span></div>
    <div class="row"><svg width="22" height="22" viewBox="0 0 22 22"><path d="M1 1h20v14H9l-6 5v-5H1z" fill="none" stroke="#5aa9dc"/></svg><div class="div" style="left:331px"></div><div class="div" style="left:409px"></div><span class="title">How to be an Investor...</span><span class="desc">How to choose what you invest in</span><span class="num c">52</span><span class="num v">249</span><span class="act">12 August 2011 &nbsp;- &nbsp;11:05 AM<br>By <b>JulesBrad</b></span></div>
  </div>
</div>

<div class="abs char" role="img" aria-label="Mascot characters peeking in from the right edge" style="left:1018px;top:338px;width:82px;height:110px;background:linear-gradient(90deg,#2b2b2b 40%,#f7b03b 40%);opacity:.85"></div>
<div class="abs char" role="img" aria-label="Large bulb mascot in glasses with a green body" style="left:55px;top:632px;width:142px;height:175px;background:linear-gradient(#f7a531 0 55%,#33a244 55%)"></div>
<div class="abs char" role="img" aria-label="Small bulb mascot with moustache" style="left:212px;top:735px;width:50px;height:70px;background:linear-gradient(#f7b03b 0 60%,#2b2b2b 60%)"></div>

<div class="abs foot-links"><a>Home</a>- <a>Invest</a>- <a>Get Investment</a>- <a>How it Works</a>- <a>About Us Blog</a>- <a>Forum</a></div>

<svg class="abs sea" viewBox="0 0 1200 116" preserveAspectRatio="none">
  <path d="M0 6 Q5 0 10 6 T20 6 T30 6 T40 6 T50 6 T60 6 T70 6 T80 6 T90 6 T100 6 T110 6 T120 6 T130 6 T140 6 T150 6 T160 6 T170 6 T180 6 T190 6 T200 6 T210 6 T220 6 T230 6 T240 6 T250 6 T260 6 T270 6 T280 6 T290 6 T300 6 T310 6 T320 6 T330 6 T340 6 T350 6 T360 6 T370 6 T380 6 T390 6 T400 6 T410 6 T420 6 T430 6 T440 6 T450 6 T460 6 T470 6 T480 6 T490 6 T500 6 T510 6 T520 6 T530 6 T540 6 T550 6 T560 6 T570 6 T580 6 T590 6 T600 6 T610 6 T620 6 T630 6 T640 6 T650 6 T660 6 T670 6 T680 6 T690 6 T700 6 T710 6 T720 6 T730 6 T740 6 T750 6 T760 6 T770 6 T780 6 T790 6 T800 6 T810 6 T820 6 T830 6 T840 6 T850 6 T860 6 T870 6 T880 6 T890 6 T900 6 T910 6 T920 6 T930 6 T940 6 T950 6 T960 6 T970 6 T980 6 T990 6 T1000 6 T1010 6 T1020 6 T1030 6 T1040 6 T1050 6 T1060 6 T1070 6 T1080 6 T1090 6 T1100 6 T1110 6 T1120 6 T1130 6 T1140 6 T1150 6 T1160 6 T1170 6 T1180 6 T1190 6 T1200 6 V116 H0Z" fill="#2f82bd"/>
</svg>

<div class="abs pay-card">
  <span class="pay-name">PayWell</span>
  <div class="pay-strip"><i></i><i></i><i></i><i></i><i></i><i></i></div>
</div>

<div class="abs social" style="left:436px"><i></i>Follow Us On Chirper</div>
<div class="abs social" style="left:672px"><i></i>Join Our Friendbook Group</div>

<div class="abs char" role="img" aria-label="Winged angel bulb mascot" style="left:976px;top:851px;width:62px;height:65px;background:linear-gradient(#f7b03b 0 50%,#d5dde4 50%);border-radius:30px 30px 0 0"></div>
<div class="abs copy">Ideaora © 2011 Copyright</div>
</body>
</html>
```